Poster of Core Values & Motto

Create our core values poster and motto. Attached are our core values and our Motto. This poster represents both of our companies Tidy Pulp & CuraBinix.

Target Market(s)

Our team / employees

Industry/Entity Type

Shredding and Medical Waste

Colors
59FF00
82FF00
B8FF75
E3FFCB
F4FFEA
EB3D1F
EC4F4E
F09395
F8D3D4
FCEDEE

Requirements
Must have
• Include both companies logos

```html
<!DOCTYPE html>
<html lang="en">
<head>
<meta charset="utf-8">
<title>Core Values &amp; Motto Poster</title>
<link href="https://fonts.googleapis.com/css2?family=Anton&family=Fira+Sans:wght@400;500&family=Signika:wght@700&display=swap" rel="stylesheet">
<style>
  :root {
    --stage: #e9e9e9;
    --header-red: #eb3d1f;
    --paper: #ffffff;
    --field-edge: #dfe0e3;
    --field-mid: #f4f4f5;
    --orange: #f26b23;
    --indigo: #5462ad;
    --purple: #ae4fb2;
    --green: #92cd70;
    --cyan: #12b8dd;
    --coral: #e45c5e;
    --brand-green: #4cbf1c;
    --brand-red: #eb3d1f;
  }
  * { box-sizing: border-box; margin: 0; padding: 0; }
  html, body { width: 1200px; height: 1200px; overflow: hidden; }
  body { background: var(--stage); position: relative; }

  .poster {
    position: absolute; left: 200px; top: 0;
    width: 800px; height: 1200px; background: var(--paper);
    overflow: hidden;
  }
  .poster-header {
    position: absolute; left: 0; top: 0; width: 800px; height: 141px;
    background: var(--header-red);
    display: flex; align-items: center; justify-content: center;
  }
  .poster-title {
    font-family: "Anton", sans-serif; font-weight: 400;
    font-size: 84px; line-height: 1; color: #fff; letter-spacing: 0.5px;
    text-shadow: 2px 3px 4px rgba(0,0,0,0.25);
    padding-top: 6px;
  }
  .values-field {
    position: absolute; left: 0; top: 141px; width: 800px; height: 926px;
    background: radial-gradient(ellipse at 50% 45%, #ffffff 0%, var(--field-mid) 45%, var(--field-edge) 100%);
  }

  .value-card {
    position: absolute; width: 334px; height: 228px;
    border: 1px solid var(--tone); border-radius: 28px;
    background: rgba(255,255,255,0.85);
  }
  .value-card .card-face {
    position: absolute; left: 7px; top: 5px; right: 7px; bottom: 5px;
    background: var(--tone); border-radius: 24px;
    box-shadow: 0 2px 4px rgba(0,0,0,0.18);
    display: flex; flex-direction: column; align-items: center; justify-content: center;
    text-align: center; color: #fff; padding-top: 30px;
  }
  .value-name {
    font-family: "Signika", sans-serif; font-weight: 700; font-size: 30px; line-height: 1.2;
    text-shadow: 0 1px 2px rgba(0,0,0,0.25); margin-bottom: 8px;
  }
  .value-motto {
    font-family: "Fira Sans", sans-serif; font-weight: 400; font-size: 24px; line-height: 1.15;
    text-shadow: 0 1px 2px rgba(0,0,0,0.2);
  }
  .value-icon {
    position: absolute; left: 50%; top: -52px; transform: translateX(-50%);
    width: 94px; height: 94px; border-radius: 50%;
    border: 1px solid var(--tone); background: #fff;
    display: flex; align-items: center; justify-content: center;
  }
  .icon-disc {
    width: 84px; height: 84px; border-radius: 50%;
    background: radial-gradient(circle at 50% 80%, rgba(255,255,255,0.55) 0%, var(--tone) 75%);
    box-shadow: inset 0 0 0 2px rgba(255,255,255,0.6);
    display: flex; align-items: center; justify-content: center;
  }
  .icon-disc svg { width: 52px; height: 52px; fill: none; stroke: #fff; stroke-width: 2; stroke-linecap: round; stroke-linejoin: round; }

  .card-teamwork { --tone: var(--orange); left: 53px; top: 69px; }
  .card-secure   { --tone: var(--indigo); left: 419px; top: 69px; }
  .card-excellence { --tone: var(--purple); left: 53px; top: 371px; }
  .card-honesty  { --tone: var(--green); left: 419px; top: 371px; }
  .card-efficient { --tone: var(--cyan); left: 53px; top: 681px; }
  .card-dependable { --tone: var(--coral); left: 419px; top: 681px; }
  .card-excellence .card-face, .card-honesty .card-face { justify-content: flex-start; padding-top: 80px; }

  .brand-footer {
    position: absolute; left: 0; top: 1067px; width: 800px; height: 133px;
    background: var(--paper);
    display: flex; align-items: center; justify-content: space-around; padding: 0 40px;
  }
  .brand { display: flex; align-items: center; gap: 12px; }
  .brand-name { font-family: "Fira Sans", sans-serif; font-weight: 500; font-size: 44px; line-height: 1; }
  .brand-tidy .brand-name { color: var(--brand-green); }
  .brand-tidy .brand-dot { width: 34px; height: 34px; border-radius: 50%; background: var(--brand-green); }
  .brand-cura .brand-name { color: var(--brand-red); }
  .brand-cura .brand-dot { width: 30px; height: 30px; background: var(--brand-red); }
</style>
</head>
<body>
  <main class="poster">
    <header class="poster-header">
      <h1 class="poster-title">CORE VALUES &amp; MOTTO</h1>
    </header>

    <section class="values-field">
      <article class="value-card card-teamwork">
        <div class="card-face">
          <h2 class="value-name">Synergy/ Teamwork</h2>
          <p class="value-motto">Get It Done Attitude<br>with Humble confidence</p>
        </div>
        <div class="value-icon"><div class="icon-disc">
          <svg viewBox="0 0 52 52" role="img" aria-label="Team and handshake icon">
            <circle cx="17" cy="13" r="4"/><circle cx="26" cy="10" r="4"/><circle cx="35" cy="13" r="4"/>
            <path d="M10 26c0-5 3-8 7-8M42 26c0-5-3-8-7-8M19 22c0-5 3-7 7-7s7 2 7 7"/>
            <path d="M6 32l8-4 8 4 6-2 6 2 8-4 4 2M14 28l10 12 4 2 8-8M22 36l4 4M18 34l4 4"/>
          </svg>
        </div></div>
      </article>

      <article class="value-card card-secure">
        <div class="card-face">
          <h2 class="value-name">Safe and Secure</h2>
          <p class="value-motto">We are just as secure<br>as an armored<br>truck with money</p>
        </div>
        <div class="value-icon"><div class="icon-disc">
          <svg viewBox="0 0 52 52" role="img" aria-label="Shield with padlock icon">
            <path d="M26 5l16 6v12c0 11-7 19-16 23C17 42 10 34 10 23V11z"/>
            <rect x="19" y="24" width="14" height="11" rx="1.5"/>
            <path d="M21 24v-4a5 5 0 0 1 10 0v4M26 28v3"/>
          </svg>
        </div></div>
      </article>

      <article class="value-card card-excellence">
        <div class="card-face">
          <h2 class="value-name">Excellence</h2>
          <p class="value-motto">Exceed expectations<br>with a smile</p>
        </div>
        <div class="value-icon"><div class="icon-disc">
          <svg viewBox="0 0 52 52" role="img" aria-label="Star and thumbs up icon">
            <path d="M22 5l3 6 6 1-4.5 4 1 6-5.5-3-5.5 3 1-6L13 12l6-1z"/>
            <path d="M10 6l3 3M34 6l-3 3M8 16h3M36 16h-3"/>
            <rect x="12" y="34" width="6" height="12"/>
            <path d="M18 35l6-8c2-2 4 0 3 2l-2 5h10c2 0 3 2 2 3l-2 8c0 1-1 1-2 1H18"/>
          </svg>
        </div></div>
      </article>

      <article class="value-card card-honesty">
        <div class="card-face">
          <h2 class="value-name">Honesty/Integrity</h2>
          <p class="value-motto">Do the right thing</p>
        </div>
        <div class="value-icon"><div class="icon-disc">
          <svg viewBox="0 0 52 52" role="img" aria-label="Connected gears icon">
            <circle cx="26" cy="26" r="6"/><circle cx="26" cy="26" r="2"/>
            <circle cx="9" cy="9" r="3.5"/><circle cx="43" cy="9" r="3.5"/>
            <circle cx="9" cy="43" r="3.5"/><circle cx="43" cy="43" r="3.5"/>
            <path d="M12 12l9 9M40 12l-9 9M12 40l9-9M40 40l-9-9M26 17v-3M26 35v3M17 26h-3M35 26h3"/>
          </svg>
        </div></div>
      </article>

      <article class="value-card card-efficient">
        <div class="card-face">
          <h2 class="value-name">Efficient</h2>
          <p class="value-motto">On-Time, sense of urgency,<br>always trying to improve</p>
        </div>
        <div class="value-icon"><div class="icon-disc">
          <svg viewBox="0 0 52 52" role="img" aria-label="Hand holding gear with tick icon">
            <circle cx="30" cy="17" r="9"/>
            <path d="M30 5v3M30 26v3M18 17h3M39 17h3M22 9l2 2M36 23l2 2M38 9l-2 2M24 23l-2 2"/>
            <path d="M26 17l3 3 5-6"/>
            <path d="M5 38h6l8-3h9c2 0 2 3 0 3h-7M21 38l13-4c3-1 5 2 2 3l-14 7H11"/>
            <rect x="3" y="35" width="6" height="11"/>
          </svg>
        </div></div>
      </article>

      <article class="value-card card-dependable">
        <div class="card-face">
          <h2 class="value-name">Dependable</h2>
          <p class="value-motto">Do what you say<br>you will do</p>
        </div>
        <div class="value-icon"><div class="icon-disc">
          <svg viewBox="0 0 52 52" role="img" aria-label="Process flowchart icon">
            <rect x="9" y="5" width="34" height="42" rx="2"/>
            <path d="M9 11h34"/>
            <rect x="20" y="16" width="16" height="5"/><rect x="20" y="26" width="16" height="5"/><rect x="20" y="36" width="16" height="5"/>
            <path d="M13 18h7M13 18v10h7M40 18v10h-4M40 28v10h-4"/>
          </svg>
        </div></div>
      </article>
    </section>

    <footer class="brand-footer">
      <div class="brand brand-tidy"><span class="brand-dot"></span><span class="brand-name">Tidy Pulp</span></div>
      <div class="brand brand-cura"><span class="brand-dot"></span><span class="brand-name">CuraBinix</span></div>
    </footer>
  </main>
</body>
</html>
```